Explosive, chemical reaction of creativity!

Web design for a digital marketing company. The unconventional is encouraged!
This is for a cool, young, geographically diverse company (artmingle... you are all part of our team!!!)... we build websites but our real specialty is "search experience optimization".... creating conversion focused content, SEO (including content), and social media.

Target Market(s)

small to medium size businesses, law firms, medical practices, municipalities

Industry/Entity Type

Marketing

Number of Pages Required

2 page

Requirements
Must have
• WOW
• something different and special... we've been playing with a science theme (www.vexmorrow.marketing) but we are open to different looks, layouts, etc.
• we nee a homepage design and an interior page design
• content needs to include: Marketing Catalysts (about us), Our Formula (services), Chemical Reactions(Results/Our Clients),
• FREE Web Prism Audit
• Let us put together an objective snapshot of your digital presence for you.
Nice to have
• we are open to the use of background video (chemical reaction???)
• we are open to cool and different imagery
Should not have
• template look like most other websites

```html
<!DOCTYPE html>
<html lang="en">
<head>
<meta charset="utf-8">
<title>Vexmorrow Marketing</title>
<link href="https://fonts.googleapis.com/css2?family=Lato:wght@300;400;700;900&family=Raleway:wght@300;400&display=swap" rel="stylesheet">
<style>
:root{
  --white:#ffffff;
  --paper:#ebebeb;
  --ink:#1c1c1c;
  --navy:#1f2f5a;
  --blue:#29abe2;
  --dark:#2f3134;
  --slate:#5c6165;
  --charcoal:#4b4b4b;
  --footer:#2a2a2a;
  --line:rgba(255,255,255,.55);
}
*{margin:0;padding:0;box-sizing:border-box}
html,body{width:1200px;height:3854px;overflow:hidden}
body{position:relative;background:var(--paper);font-family:'Lato',sans-serif;color:var(--ink)}
.backdrop{position:absolute;left:0;top:0}
.abs{position:absolute}
.center{left:0;width:1200px;text-align:center}
.site-header{position:absolute;left:0;top:0;width:1200px;height:108px}
.brand{position:absolute;left:77px;top:28px;display:flex;align-items:center;gap:14px}
.brand-mark{width:44px;height:44px;background:var(--navy)}
.brand-name{font-weight:900;font-size:27px;letter-spacing:2px;color:var(--navy);text-transform:uppercase;line-height:1}
.nav{position:absolute;top:62px;left:580px;display:flex;gap:30px;font-size:13px;font-weight:700;color:var(--ink)}
.nav .active{border-bottom:2px solid var(--ink);padding-bottom:6px}
.social{position:absolute;display:flex;gap:10px}
.social span{width:26px;height:26px;border-radius:50%;border:1.5px solid currentColor;display:block}
.hero-title{top:196px;font-family:'Raleway',sans-serif;font-weight:300;font-size:56px;line-height:66px;color:var(--white)}
.hero-sub{top:336px;font-size:19px;line-height:30px;color:var(--white)}
.btn-outline{border:2px solid var(--white);color:var(--white);font-weight:700;letter-spacing:1px;text-transform:uppercase;display:flex;align-items:center;justify-content:center}
.hero-btn{left:493px;top:411px;width:214px;height:64px;font-size:24px}
.intro-title{left:80px;top:636px;font-family:'Raleway',sans-serif;font-size:38px;font-weight:400}
.intro-lead{left:80px;top:704px;width:440px;font-size:14px;font-weight:700;line-height:21px}
.intro-text{left:80px;top:750px;width:440px;font-size:12px;font-weight:700;line-height:20px}
.philosophy{left:663px;top:681px;width:437px;height:141px;background:#1e1e1e;color:var(--white);padding:18px 22px}
.philosophy h3{font-family:'Raleway',sans-serif;font-weight:400;font-size:28px}
.philosophy strong{display:block;font-size:13px;margin-top:6px}
.philosophy p{font-size:12px;line-height:19px;margin-top:8px;color:#ddd}
.tab{left:1123px;top:658px;width:160px;height:164px;border-radius:82px;background:var(--blue)}
.tab-label{left:1164px;top:700px;writing-mode:vertical-rl;color:var(--white);font-size:15px;letter-spacing:1px}
.vline{width:2px;background:var(--line);left:599px}
.spaced{font-weight:300;letter-spacing:.5em;text-transform:uppercase;color:var(--white)}
.section-title{font-size:32px}
.service{width:320px;text-align:center;color:var(--white)}
.service h4{font-size:19px;font-weight:700;letter-spacing:2px;display:flex;align-items:center;justify-content:center;gap:12px;padding-bottom:10px;border-bottom:1px solid var(--line)}
.service p{font-size:13px;font-weight:700;line-height:20px;margin-top:14px;padding:0 30px}
.body-white{font-size:12px;font-weight:700;line-height:21px;color:var(--white)}
.team-btn{left:385px;top:1989px;width:432px;height:54px;font-size:15px;letter-spacing:.4em;border-width:1.5px}
.section-dark{font-size:30px;color:var(--ink)}
.news-card{display:flex;gap:15px;width:520px}
.news-img{width:198px;height:116px;flex:none}
.news-card h5{font-size:15px;font-weight:700;margin-top:2px}
.news-card p{font-size:12px;line-height:17px;margin-top:4px}
.news-card a{font-size:11px;font-weight:700;color:var(--ink);text-decoration:underline}
.pager{width:31px;height:41px;border:1.5px solid #555;display:flex;align-items:center;justify-content:center}
.pager.fill{background:#222}
.field{background:transparent;border:1px solid rgba(255,255,255,.7);color:var(--white);font-size:12px;padding:10px 12px;font-family:'Lato',sans-serif}
.btn-blue{background:var(--blue);color:var(--white);font-size:15px;letter-spacing:2px;text-transform:uppercase;display:flex;align-items:center;justify-content:center}
.contact{display:flex;align-items:center;gap:16px;color:var(--white)}
.contact .ring{width:52px;height:52px;border-radius:50%;border:1.5px solid rgba(255,255,255,.6);display:flex;align-items:center;justify-content:center}
.contact small{display:block;font-size:12px;letter-spacing:1px;color:#bbb}
.contact b{font-size:12px;font-weight:700}
.copyright{left:80px;top:3784px;font-size:11px;color:#ccc}
</style>
</head>
<body>

<svg class="backdrop" width="1200" height="3854" viewBox="0 0 1200 3854">
  <defs>
    <linearGradient id="heroFill" x1="0" y1="0" x2="1" y2="1">
      <stop offset="0" stop-color="#183a66"/><stop offset=".5" stop-color="#3c7fb4"/><stop offset="1" stop-color="#10243f"/>
    </linearGradient>
    <radialGradient id="moleculeFill" cx=".75" cy=".3" r=".8">
      <stop offset="0" stop-color="#474c52"/><stop offset="1" stop-color="#26282b"/>
    </radialGradient>
    <linearGradient id="teamFill" x1="0" y1="0" x2="1" y2="0">
      <stop offset="0" stop-color="#6b5a4e"/><stop offset=".5" stop-color="#3b3d42"/><stop offset="1" stop-color="#2c2f36"/>
    </linearGradient>
  </defs>
  <rect x="0" y="0" width="1200" height="108" fill="#ffffff"/>
  <polygon role="img" aria-label="Hero image: glossy molecular model over a swirling blue background" points="0,108 1200,108 1200,475 617,617 0,475" fill="url(#heroFill)"/>
  <polygon role="img" aria-label="Services backdrop: dark molecular structure of linked spheres" points="0,879 1200,879 1200,1440 0,1200" fill="url(#moleculeFill)"/>
  <polygon points="0,1200 1200,1440 1200,1700 0,1580" fill="var(--slate)"/>
  <polygon role="img" aria-label="Team photo: smiling colleagues in a bright office, darkened overlay" points="0,1580 1200,1700 1200,1953 0,2313" fill="url(#teamFill)"/>
  <polygon points="0,2313 1200,1953 1200,2580 0,2480" fill="#e9e9e9"/>
  <rect role="img" aria-label="Footer backdrop: faint dark street map" x="0" y="2900" width="1200" height="954" fill="var(--footer)"/>
  <polygon points="0,2480 1200,2580 1200,2981 600,3148 0,2981" fill="var(--charcoal)"/>
  <rect x="0" y="3752" width="1200" height="102" fill="#252525"/>
  <line x1="0" y1="3752" x2="1200" y2="3752" stroke="#555" stroke-width="1"/>
</svg>

<header class="site-header">
  <div class="brand"><span class="brand-mark"></span><span class="brand-name">Vexmorrow Marketing</span></div>
  <nav class="nav">
    <span class="active">Home</span><span>Marketing Catalysts</span><span>Our Formula</span><span>Chemical Reactions</span><span>Contact Us</span>
  </nav>
  <div class="social" style="left:1020px;top:18px;color:#333"><span></span><span></span><span></span></div>
</header>

<h1 class="abs center hero-title">It's not rocket science,<br>it's Vexmorrow science!</h1>
<p class="abs center hero-sub">Sales is the chemical reaction that results from "our formula" which is the right<br>combination of our digital marketing services.</p>
<div class="abs btn-outline hero-btn">Get Started</div>

<h2 class="abs intro-title">Using data for success</h2>
<p class="abs intro-lead">Search Engine Optimization has been replaced with Search Experience Optimization.</p>
<p class="abs intro-text">Lorem ipsum dolor sit amet, consectetuer adipiscing elit, seddiam nonummy nibh euismod . Lorem ipsum dolor sit amet, consectetuer adipiscing elit, seddiam nonummy .</p>
<div class="abs philosophy">
  <h3>Our Business Philosophy</h3>
  <strong>Lorem ipsum dolor sit amet consectetur</strong>
  <p>Lorem ipsum dolor sit amet, consectetuer adipiscing elit, seddiam nonummy nibh euismod .</p>
</div>
<div class="abs tab"></div>
<svg class="abs" style="left:1130px;top:720px" width="22" height="40" viewBox="0 0 22 40"><polyline points="3,3 19,20 3,37" fill="none" stroke="#fff" stroke-width="2"/></svg>
<span class="abs tab-label">Get in Touch</span>

<div class="abs vline" style="top:905px;height:58px"></div>
<h2 class="abs center spaced section-title" style="top:988px">Services</h2>
<div class="abs service" style="left:79px;top:1058px">
  <h4><svg width="28" height="18" viewBox="0 0 28 18"><path d="M7 17h15a5 5 0 0 0 0-10 7 7 0 0 0-13-1A5.5 5.5 0 0 0 7 17z" fill="#fff"/></svg>Website</h4>
  <p>You've got 10 seconds to grab the attention of a site viewer. We build for appearance, content, and functionality.</p>
</div>
<div class="abs service" style="left:439px;top:1058px">
  <h4><svg width="26" height="20" viewBox="0 0 26 20"><rect x="1" y="1" width="24" height="15" rx="2" fill="#fff"/><circle cx="13" cy="8.5" r="3.5" fill="#2f3134"/><rect x="8" y="17" width="10" height="2" fill="#fff"/></svg>Content</h4>
  <p>Content is the most powerful element of our formula... It creates need, provokes emotion and sparks action.</p>
</div>
<div class="abs service" style="left:799px;top:1058px">
  <h4><svg width="20" height="20" viewBox="0 0 20 20"><circle cx="15" cy="4" r="3" fill="#fff"/><circle cx="4" cy="10" r="3" fill="#fff"/><circle cx="15" cy="16" r="3" fill="#fff"/><path d="M15 4 4 10 15 16" fill="none" stroke="#fff" stroke-width="1.6"/></svg>Social</h4>
  <p>We are obsessed with the latest trends and are always testing new ways to cultivate both following and engagement.</p>
</div>

<div class="abs vline" style="top:1440px;height:62px"></div>
<h2 class="abs center spaced section-title" style="top:1522px">Mission</h2>
<p class="abs body-white" style="left:290px;top:1574px;width:620px;text-align:center">Lorem ipsum dolor sit amet, consectetuer adipiscing elit, seddiam nonummy nibh euismod . Lorem ipsum dolor sit amet Lorem ipsum dolor sit .Lorem ipsum dolor sit amet, consectetuer adipiscing elit, seddiam nonummy nibh euismod . Lorem ipsum dolor sit amet Lorem ipsum dolor sit .</p>

<div class="abs vline" style="top:1775px;height:62px"></div>
<h2 class="abs center spaced section-title" style="top:1862px">Meet the Team</h2>
<p class="abs body-white" style="left:290px;top:1922px;width:620px;text-align:center">Lorem ipsum dolor sit amet, consectetuer adipiscing elit, seddiam nonummy nibh euismod . Lorem ipsum dolor sit amet Lorem ipsum dolor sit .Lorem ipsum dolor sit amet, consectetuer .</p>
<div class="abs btn-outline team-btn">Read More</div>

<div class="abs vline" style="top:2185px;height:56px;background:#555"></div>
<h2 class="abs center spaced section-dark" style="top:2250px">Latest News</h2>
<article class="abs news-card" style="left:80px;top:2344px">
  <div class="news-img" role="img" aria-label="News photo: hands using a tablet on a desk" style="background:linear-gradient(135deg,#c9d2dc,#8a97a5)"></div>
  <div><h5>Lorem ipsum dolor sit amet, consectet</h5><p>Lorem ipsum dolor sit amet, consectetuer adipiscing elit. Sed vitae magna tellus. Aenean ante nunc, semper nec cursus</p><a>Read More »</a></div>
</article>
<article class="abs news-card" style="left:617px;top:2344px">
  <div class="news-img" role="img" aria-label="News photo: laptop on a workspace with a coffee cup" style="background:linear-gradient(135deg,#9aa0a6,#4a4f55)"></div>
  <div><h5>Lorem ipsum dolor sit amet, consectet</h5><p>Lorem ipsum dolor sit amet, consectetuer adipiscing elit. Sed vitae magna tellus. Aenean ante nunc, semper nec cursus</p><a>Read More »</a></div>
</article>
<div class="abs pager" style="left:1043px;top:2490px"><svg width="10" height="16" viewBox="0 0 10 16"><polyline points="8,2 2,8 8,14" fill="none" stroke="#333" stroke-width="2"/></svg></div>
<div class="abs pager fill" style="left:1090px;top:2490px"><svg width="10" height="16" viewBox="0 0 10 16"><polyline points="2,2 8,8 2,14" fill="none" stroke="#fff" stroke-width="2"/></svg></div>

<div class="abs vline" style="top:2686px;height:76px"></div>
<h2 class="abs center spaced section-title" style="top:2806px">Newsletter Signup</h2>
<div class="abs" style="left:378px;top:2871px;width:444px;height:36px;background:#fff;font-size:12px;color:#777;display:flex;align-items:center;justify-content:center">Enter Your Email Here</div>
<div class="abs btn-blue" style="left:524px;top:2938px;width:152px;height:37px">Subscribe</div>

<div class="abs vline" style="top:3187px;height:64px"></div>
<h2 class="abs center spaced" style="top:3282px;font-size:34px">Free Web Prism Audit</h2>
<div class="abs field" style="left:321px;top:3367px;width:267px;height:36px">Name</div>
<div class="abs field" style="left:607px;top:3367px;width:269px;height:36px">Email</div>
<div class="abs field" style="left:321px;top:3421px;width:267px;height:36px">Phone</div>
<div class="abs field" style="left:607px;top:3421px;width:269px;height:36px;display:flex;justify-content:space-between">Subject<span>▾</span></div>
<div class="abs field" style="left:321px;top:3475px;width:555px;height:59px">Message</div>
<div class="abs btn-blue" style="left:524px;top:3560px;width:152px;height:38px">Submit</div>

<div class="abs contact" style="left:277px;top:3656px">
  <span class="ring"><svg width="18" height="24" viewBox="0 0 18 24"><path d="M9 1a8 8 0 0 0-8 8c0 6 8 14 8 14s8-8 8-14a8 8 0 0 0-8-8z" fill="#fff"/><circle cx="9" cy="9" r="3" fill="#2a2a2a"/></svg></span>
  <div><b>VEXMORROW MARKETING</b><br><b style="font-weight:400">2870 Harlow Avenue Suite 210</b><br><b style="font-weight:400">Dunmore, TX 78090</b></div>
</div>
<div class="abs contact" style="left:645px;top:3656px">
  <span class="ring"><svg width="22" height="22" viewBox="0 0 22 22"><path d="M5 1l4 5-2.5 2.5a12 12 0 0 0 7 7L16 13l5 4-3 4C9 21 1 13 1 4z" fill="#fff"/></svg></span>
  <div><small>CALL US TODAY</small><span style="font-size:24px;font-weight:700">866-555-0142</span></div>
</div>

<p class="abs copyright">Copyright © 2016 VEXMORROW MARKETING . All Right Reserved</p>
<div class="social" style="left:1023px;top:3777px;color:#bbb"><span></span><span></span><span></span></div>

</body>
</html>
```